Furniture restoration to chairs. Hand weaving.

Industry/Entity Type

Furniture

Contact Information for Business Card

The Wicker Loom
Cane, rush, splint and shaker tape.
482 Fenn Rd
Gull Cove
ME 04913
207 - 555 - 0183
Cell: 207 - 555 - 0276

For graphics I want a picture of a caned rocking chair or maybe a rush and a cane chair.

```html
<!DOCTYPE html>
<html lang="en">
<head>
<meta charset="utf-8">
<title>The Wicker Loom – Business Card</title>
<link href="https://fonts.googleapis.com/css2?family=Roboto:wght@400;700;900&display=swap" rel="stylesheet">
<style>
  :root {
    --page-bg: #3a2a22;
    --card-light: #e8e3d8;
    --card-dark: #2b2826;
    --gold: #b0813a;
    --ink: #1c1a18;
    --photo-a: #a8703a;
    --photo-b: #c99a58;
  }
  * { margin: 0; padding: 0; box-sizing: border-box; }
  html, body {
    width: 1200px; height: 1200px; overflow: hidden;
    background: var(--page-bg);
    font-family: "Roboto", Arial, sans-serif;
  }
  .card {
    position: absolute; left: 73px; top: 300px;
    width: 1054px; height: 600px;
    background: var(--card-dark);
    box-shadow: 0 10px 30px rgba(0,0,0,.45);
    overflow: hidden;
  }
  .card-shapes { position: absolute; inset: 0; }
  .brand {
    position: absolute; left: 60px; top: 112px; width: 400px;
    text-align: center; color: var(--gold);
  }
  .brand-article {
    display: flex; align-items: center; justify-content: center; gap: 22px;
    font-size: 34px; font-weight: 400; line-height: 1;
  }
  .brand-article::before, .brand-article::after {
    content: ""; width: 116px; height: 2px; background: var(--gold);
  }
  .brand-name {
    font-size: 52px; font-weight: 700; line-height: 1; margin-top: 10px;
    letter-spacing: -0.5px;
  }
  .tagline {
    position: absolute; left: 60px; top: 245px; width: 400px;
    text-align: center; color: var(--ink);
    font-size: 27px; font-weight: 700; line-height: 35px;
  }
  .furniture-photo {
    position: absolute; left: 31px; top: 360px; width: 425px; height: 185px;
    background: linear-gradient(90deg, var(--photo-a), var(--photo-b) 50%, var(--photo-a));
    opacity: .85;
  }
  .contact {
    position: absolute; right: 72px; top: 113px;
    text-align: right; color: var(--gold);
    font-size: 28px; line-height: 35px;
  }
  .contact-name { font-size: 43px; font-weight: 700; line-height: 46px; margin-right: -6px; }
  .contact-role { margin-bottom: 38px; }
  .contact-email { margin-bottom: 27px; margin-right: 5px; }
  .contact-phones { margin-bottom: 32px; margin-right: 2px; }
  .contact-address { margin-right: 6px; }
</style>
</head>
<body>
  <section class="card">
    <svg class="card-shapes" width="1054" height="600" viewBox="0 0 1054 600" aria-hidden="true">
      <polygon points="0,0 422,0 661,600 0,600" fill="var(--card-light)"/>
      <polygon points="581,400 431,600 661,600" fill="var(--gold)"/>
    </svg>

    <div class="brand">
      <div class="brand-article">THE</div>
      <div class="brand-name">WICKER LOOM</div>
    </div>

    <p class="tagline">CANE, RUSH, SPLINT<br>AND SHAKER TAPE.</p>

    <div class="furniture-photo" role="img" aria-label="Photo of a woven rattan rocking chair, a small wicker side table and a wicker armchair"></div>

    <div class="contact">
      <div class="contact-name">YOUR NAME HERE</div>
      <div class="contact-role">DIRECTOR</div>
      <div class="contact-email">your@email.com</div>
      <div class="contact-phones">207 - 555 - 0183<br>207 - 555 - 0276</div>
      <div class="contact-address">482 FENN RD<br>GULL COVE<br>ME 04913</div>
    </div>
  </section>
</body>
</html>
```